jpg 'poster' for music show to use on social media (only 72dpi needed)

style wanted: Nils Ardent goes western

text:

Rick Talver
Dana Pruckett
Glen Ostrava
Marisol Tadcastle
... and friends

Friday April 25
Millpond Coffee
Seattle

7:00 PM

$5

would love to get ASAP.

committed to pay for a cool poster!
just need 72 dpi. Thx!

not crazy particular. a cool Nils Ardent type layout will be accepted :)

```html
<!DOCTYPE html>
<html lang="en">
<head>
<meta charset="utf-8">
<title>Millpond — Friday, April 25</title>
<link rel="stylesheet" href="https://fonts.googleapis.com/css2?family=Amatic+SC:wght@400;700&family=Marcellus+SC&display=swap">
<style>
  :root {
    --board-dark: #1f1f1f;
    --board-mid: #3b3b3b;
    --board-light: #4a4a4a;
    --chalk: #f2f2f2;
    --chalk-soft: #d9d9d9;
  }
  * { box-sizing: border-box; }
  html, body {
    margin: 0;
    padding: 0;
    width: 927px;
    height: 1200px;
    overflow: hidden;
    background: var(--board-dark);
  }
  .poster {
    position: relative;
    width: 927px;
    height: 1200px;
    overflow: hidden;
    background:
      radial-gradient(ellipse at 55% 40%, var(--board-light) 0%, var(--board-mid) 45%, var(--board-dark) 100%);
    color: var(--chalk);
    font-family: "Amatic SC", "Arial Narrow", sans-serif;
  }
  .poster p, .poster h1, .poster ul, .poster li { margin: 0; padding: 0; }

  .masthead {
    position: absolute;
    top: 40px;
    left: 0;
    width: 927px;
    text-align: center;
    font-family: "Marcellus SC", Georgia, serif;
    font-size: 98px;
    line-height: 98px;
    letter-spacing: 4px;
    font-weight: 400;
  }
  .masthead-dash {
    position: absolute;
    top: 88px;
    height: 3px;
    background: var(--chalk);
    border-radius: 2px;
  }
  .masthead-dash--left { left: 30px; width: 84px; }
  .masthead-dash--right { left: 818px; width: 88px; }

  .lineup {
    position: absolute;
    top: 0;
    left: 71px;
    list-style: none;
  }
  .lineup-act {
    position: absolute;
    left: 0;
    white-space: nowrap;
    text-transform: uppercase;
    font-size: 60px;
    line-height: 60px;
    font-weight: 700;
    letter-spacing: 5px;
  }
  .guitar-art {
    position: absolute;
    left: 621px;
    top: 220px;
    width: 190px;
    height: 447px;
  }
  .price {
    position: absolute;
    top: 752px;
    left: 0;
    width: 927px;
    text-align: center;
    text-transform: uppercase;
    font-size: 66px;
    line-height: 66px;
    font-weight: 400;
    letter-spacing: 5px;
    color: var(--chalk-soft);
  }
  .divider {
    position: absolute;
    background: var(--chalk);
    border-radius: 3px;
  }
  .divider--thick { left: 61px; top: 853px; width: 757px; height: 5px; }
  .divider--thin { left: 129px; top: 877px; width: 757px; height: 3px; }

  .event-details {
    position: absolute;
    top: 0;
    left: 0;
    width: 927px;
    text-align: center;
  }
  .event-line {
    position: absolute;
    left: 0;
    width: 927px;
    text-transform: uppercase;
    font-size: 60px;
    line-height: 60px;
    font-weight: 700;
    letter-spacing: 3px;
  }
  .event-date { top: 924px; }
  .event-venue { top: 1006px; }
  .event-time {
    top: 1092px;
    font-size: 76px;
    line-height: 76px;
    font-weight: 400;
    letter-spacing: 10px;
    color: var(--chalk-soft);
  }
</style>
</head>
<body>
  <main class="poster">
    <span class="masthead-dash masthead-dash--left"></span>
    <h1 class="masthead">MILLPOND</h1>
    <span class="masthead-dash masthead-dash--right"></span>

    <ul class="lineup">
      <li class="lineup-act" style="top:236px">Rick Talver</li>
      <li class="lineup-act" style="top:331px">Dana Pruckett</li>
      <li class="lineup-act" style="top:428px">Glen Ostrava</li>
      <li class="lineup-act" style="top:526px">Marisol Tadcastle</li>
      <li class="lineup-act" style="top:628px">... and friends</li>
    </ul>

    <svg class="guitar-art" viewBox="0 0 190 447" role="img" aria-label="Chalk line drawing of an acoustic guitar">
      <rect x="0" y="0" width="190" height="447" rx="40" fill="#555555" opacity="0.55"/>
    </svg>

    <p class="price">Only $5</p>

    <span class="divider divider--thick"></span>
    <span class="divider divider--thin"></span>

    <div class="event-details">
      <p class="event-line event-date">Friday, April 25</p>
      <p class="event-line event-venue">at Millpond Coffee</p>
      <p class="event-line event-time">7:00 PM</p>
    </div>
  </main>
</body>
</html>
```